Flier redesign

Sample fliers are attached from previous 2 years "Seasonal care 2018" and "2019 Seasonal Care" . Need an updated design for this year.

Possible images are attached to this brief. If you use the before/after pictures - you should use both of them. Use images attached to this brief or any from our website that you may prefer.

Colors

Designer to choose colors to be used in the design.

Requirements
Must have
• Colors should match our website theme. www.hollowbrookgardens.org
• Should be a "new" design, not just copying one of the prior year designs with a different image.
• Must be created in photoshop and file must be provided at the end.
• Text should be the same as 2019 version.

```html
<!DOCTYPE html>
<html lang="en">
<head>
<meta charset="utf-8">
<title>Hollowbrook Gardens – Grave Care Plans</title>
<link rel="stylesheet" href="https://fonts.googleapis.com/css2?family=Barlow:wght@300;400;500;600;700&family=Barlow+Condensed:wght@500;600&display=swap">
<style>
  :root{
    --orange:#efb466;
    --white:#ffffff;
    --text:#6a6a6a;
    --dark:#555555;
    --tick:#58b947;
    --brand:#8a2b2b;
    --photo-top:#5f8a4a;
    --photo-mid:#8fb26a;
    --photo-low:#a9c97f;
  }
  *{margin:0;padding:0;box-sizing:border-box}
  html,body{width:1200px;height:1200px;overflow:hidden;background:var(--white)}
  body{position:relative;font-family:"Barlow",Arial,sans-serif;color:var(--text)}

  .flyer{position:absolute;left:136px;top:0;width:928px;height:1200px;background:var(--white)}

  .hero-photo{position:absolute;left:0;top:0;width:928px;height:588px;
    background:linear-gradient(180deg,var(--photo-top) 0%,var(--photo-mid) 55%,var(--photo-low) 100%)}
  .hero-curve{position:absolute;left:0;top:520px;width:928px;height:70px}

  .brand-tab{position:absolute;left:618px;top:0;width:310px;height:126px;background:var(--white);
    border-bottom-left-radius:60px;display:flex;align-items:center;justify-content:center;gap:10px}
  .brand-tab .dot{width:14px;height:14px;border-radius:50%;background:var(--brand)}
  .brand-tab .name{font-family:"Barlow",Arial,sans-serif;font-weight:500;font-size:20px;color:var(--brand);letter-spacing:.5px}

  .plan{position:absolute;background:var(--white);border-radius:12px;box-shadow:0 3px 10px rgba(0,0,0,.18)}
  .plan-head{position:absolute;background:var(--orange);color:var(--white);text-align:center;
    border-radius:12px 12px 0 0;clip-path:polygon(0 0,100% 0,100% 89%,50% 100%,0 89%)}
  .plan-title{font-weight:700;font-size:22px;line-height:1.15;letter-spacing:.3px}
  .plan-sub{font-weight:300;font-size:15.5px;line-height:1.3;margin-top:10px}

  .features{list-style:none;position:absolute}
  .features li{position:relative;padding-left:16px;font-size:9.5px;line-height:1.3;margin-bottom:13px;color:var(--text)}
  .features li svg{position:absolute;left:0;top:1px;width:10px;height:9px}

  .seasonal{left:94px;top:510px;width:176px;height:356px}
  .seasonal-head{left:86px;top:518px;width:196px;height:160px;padding-top:30px}
  .seasonal .features{left:8px;top:192px;width:165px}
  .seasonal .features li{font-weight:600;color:var(--dark)}
  .price-table{position:absolute;left:10px;top:284px;width:156px;display:flex}
  .price-table .col{flex:1;text-align:center;border-left:1px solid #ddd;padding:4px 0}
  .price-table .col:first-child{border-left:none}
  .price-table .term{font-family:"Barlow Condensed",sans-serif;font-size:13px;font-weight:500;color:var(--text)}
  .price-table .amt{font-family:"Barlow Condensed",sans-serif;font-size:17px;font-weight:600;color:var(--dark);margin-top:8px}

  .perpetual{left:357px;top:480px;width:211px;height:470px}
  .perpetual-head{left:352px;top:480px;width:221px;height:180px;padding-top:36px}
  .perpetual .features{left:12px;top:199px;width:195px}
  .basic{left:652px;top:510px;width:176px;height:337px}
  .basic-head{left:642px;top:518px;width:196px;height:160px;padding-top:34px}
  .basic-head .plan-sub{font-size:14px;margin-top:12px}
  .basic .features{left:8px;top:184px;width:165px}
  .basic .features li{font-size:8.5px;margin-bottom:11px}

  .payment{position:absolute;left:0;width:100%;text-align:center;color:var(--dark)}
  .payment .label{font-size:13px;line-height:1.3}
  .payment .amount{font-family:"Barlow Condensed",sans-serif;font-weight:600;font-size:26px;margin-top:6px}
  .basic .payment .label{font-size:11px}
  .basic .payment .amount{font-size:18px;margin-top:4px}

  .contact-band{position:absolute;left:0;top:1122px;width:928px;height:78px;background:var(--orange);
    color:var(--white);font-family:"Barlow Condensed",sans-serif;font-weight:500}
  .contact-band .web{position:absolute;left:30px;top:24px;font-size:27px;text-transform:uppercase}
  .contact-band .mail{position:absolute;right:24px;top:24px;font-size:27px;text-transform:uppercase}
  .contact-band .call{position:absolute;left:0;right:0;top:2px;text-align:center;font-size:36px;line-height:1}
</style>
</head>
<body>
<main class="flyer">
  <div class="hero-photo" role="img" aria-label="Photo of a leafy cemetery with rows of headstones on green lawns under tall trees"></div>
  <svg class="hero-curve" viewBox="0 0 928 70" preserveAspectRatio="none" aria-hidden="true">
    <path d="M0 68 Q464 -40 928 68 L928 70 L0 70 Z" fill="#ffffff"/>
  </svg>

  <div class="brand-tab"><span class="dot"></span><span class="name">HOLLOWBROOK GARDENS</span></div>

  <section class="plan seasonal">
    <ul class="features">
      <li><svg viewBox="0 0 10 9"><path d="M1 5 L4 8 L9 1" fill="none" stroke="#58b947" stroke-width="1.6"/></svg>Weeding and trimming services on your gravesite approximately every 7 weeks during the growing season: mid-April through mid-October</li>
    </ul>
    <div class="price-table">
      <div class="col"><div class="term">1YEAR</div><div class="amt">115$</div></div>
      <div class="col"><div class="term">2YEARS</div><div class="amt">230$</div></div>
      <div class="col"><div class="term">3YEARS</div><div class="amt">345$</div></div>
    </div>
  </section>
  <header class="plan-head seasonal-head">
    <h2 class="plan-title">SEASONAL CARE</h2>
    <p class="plan-sub">Seasonal landscaping<br>grave care</p>
  </header>

  <section class="plan perpetual">
    <ul class="features">
      <li><svg viewBox="0 0 10 9"><path d="M1 5 L4 8 L9 1" fill="none" stroke="#58b947" stroke-width="1.6"/></svg>Weeding and filming services on your gravesite approximately every. 7 weeks during the growing season: mid-April through mid-October</li>
      <li><svg viewBox="0 0 10 9"><path d="M1 5 L4 8 L9 1" fill="none" stroke="#58b947" stroke-width="1.6"/></svg>Monument leveling and cleaning</li>
      <li><svg viewBox="0 0 10 9"><path d="M1 5 L4 8 L9 1" fill="none" stroke="#58b947" stroke-width="1.6"/></svg>Payment ensures grave care forever</li>
      <li><svg viewBox="0 0 10 9"><path d="M1 5 L4 8 L9 1" fill="none" stroke="#58b947" stroke-width="1.6"/></svg>Full bed of boxwood shrubs</li>
      <li><svg viewBox="0 0 10 9"><path d="M1 5 L4 8 L9 1" fill="none" stroke="#58b947" stroke-width="1.6"/></svg>Replacement of shrubs</li>
      <li><svg viewBox="0 0 10 9"><path d="M1 5 L4 8 L9 1" fill="none" stroke="#58b947" stroke-width="1.6"/></svg>Trust certificate</li>
    </ul>
    <div class="payment" style="top:384px">
      <div class="label">12 MONTHLY<br>PAYMENTS OF</div>
      <div class="amount">297$</div>
    </div>
  </section>
  <header class="plan-head perpetual-head">
    <h2 class="plan-title">PERPETUAL CARE<br>ENDOWMENT</h2>
    <p class="plan-sub">Landscaping care forever<br>for graves with plantings.</p>
  </header>

  <section class="plan basic">
    <ul class="features">
      <li><svg viewBox="0 0 10 9"><path d="M1 5 L4 8 L9 1" fill="none" stroke="#58b947" stroke-width="1.6"/></svg>Weeding and trimming services on your gravesite 2 times per year mid-May and mid-September .</li>
      <li><svg viewBox="0 0 10 9"><path d="M1 5 L4 8 L9 1" fill="none" stroke="#58b947" stroke-width="1.6"/></svg>Monument leveling</li>
      <li><svg viewBox="0 0 10 9"><path d="M1 5 L4 8 L9 1" fill="none" stroke="#58b947" stroke-width="1.6"/></svg>Payment ensures grave care forever</li>
    </ul>
    <div class="payment" style="top:276px">
      <div class="label">12 MONTHLY<br>PAYMENTS OF</div>
      <div class="amount">239$</div>
    </div>
  </section>
  <header class="plan-head basic-head">
    <h2 class="plan-title">BASIC CARE<br>ENDOWMENT</h2>
    <p class="plan-sub">Landscaping care forever<br>for graves with no plantings</p>
  </header>

  <footer class="contact-band">
    <span class="web">www.hollowbrookgardens.org</span>
    <span class="call">CALL US<br>(201) 555-0148</span>
    <span class="mail">info@hollowbrookgardens.org</span>
  </footer>
</main>
</body>
</html>
```